Portal for Beautiful & Up-and-Coming Caribbean destination of KVT, Puerto Rico

We need the web design of an online portal for the KVT community of Puerto Rico. This should include the landing page, menu page, and at least one content page. The KVT area is a vibrant area in Northwest Puerto Rico with an airport, many local restaurants, beautiful beaches, and many things to do. I attach the logo which should be featured prominently, and we'll also be selling merchandise using this logo. The website should be a place for everyone in the community or tourists looking for things to do and places to stay. It will need to feature space and places for advertising as well. Also, we have a live hashtag feed (www.kvtvibe-demo.com) where businesses and people in the community can hashtag their posts (we have licensed software that updates it every 30 minutes). We would like for the live hashtag feed to be part of the design, though the format can be changed a bit from what is currently in place. Indeed, the landing page should be changed to emphasize both the hashtag feed as well as the content of the site of KVTvibe. We need the landing page, menu page which will include 10-15 different modules or pages (examples: restaurants, things to do, places to stay, flights). I attach a spreadsheet which shows the menu pages that need to be featured. Comparable websites in our area are www.gosulena.com and www.varelaguide.com (but I don't like either one!). The final design should be contemporary, fresh, colorful fun and current, and communicate a vibrant and interactive community.

Target Market(s)

Tourists and people who live in this beach - oriented, beautiful community

Industry/Entity Type

Community

Number of Pages Required

3 page

Font styles to use
Sans Serif

Colors
33a6d7
f68e4e

Requirements
Must have
• landing page, menu design/page, and a sample content page. It must integrate a live hashtag feed, comparable to what is currently seen on www.kvtvibe-demo.com. It must be fun, contemporary, colorful, unique, and clean. It must allow for advertising space.
Nice to have
• comments and interaction with visitors. Colors that integrate with the logo. Much emphasis on the logo, as we will also be selling merchandise.
Should not have
• extra squiggles and curlies and adornments.

```html
<!DOCTYPE html>
<html lang="en">
<head>
<meta charset="utf-8">
<title>KVTvibe – Community Portal</title>
<link rel="stylesheet" href="https://fonts.googleapis.com/css2?family=Open+Sans:wght@400;600;700&family=Fira+Sans+Condensed:wght@500;600;700&family=Merienda:wght@700&display=swap">
<style>
:root{
  --blue:#33a6d7;
  --blue-light:#5fc4ec;
  --orange:#f68e4e;
  --ink:#4a4a4a;
  --muted:#6b6b6b;
  --frame:#e6e6e6;
  --panel-bg:#efefef;
  --white:#ffffff;
  --field:rgba(40,90,140,.75);
  --dark:#2d2d2d;
}
*{box-sizing:border-box;margin:0;padding:0}
html,body{width:1200px;height:3371px;overflow:hidden}
body{background:var(--frame);font-family:"Open Sans",Arial,sans-serif;color:var(--ink);position:relative}
.page{position:absolute;left:16px;top:16px;width:1168px;height:3332px;background:var(--panel-bg)}
.abs{position:absolute}

/* Hero */
.hero{position:absolute;left:16px;top:16px;width:1168px;height:690px;overflow:hidden;
  background:linear-gradient(180deg,#4f6b8f 0%,#8a8fa6 22%,#c9a98f 40%,#8d8167 58%,#5b5a40 75%,#3d3a2c 100%)}
.hero-photo{position:absolute;inset:0;background:
  radial-gradient(ellipse at 25% 55%,rgba(80,110,50,.55),transparent 45%),
  radial-gradient(ellipse at 80% 70%,rgba(60,50,40,.5),transparent 40%),
  linear-gradient(90deg,rgba(140,90,60,.35),transparent 30%)}
.hero-wave{position:absolute;left:0;bottom:-1px;width:1168px;height:60px}
.brand{position:absolute;left:45px;top:70px;font-family:"Open Sans",sans-serif;font-weight:700;font-size:62px;color:var(--orange);letter-spacing:-1px;line-height:1}
.social{position:absolute;display:flex;gap:8px}
.social span{width:28px;height:28px;border-radius:50%;background:var(--white);display:block}
.social.top{left:813px;top:53px}
.search{position:absolute;left:1004px;top:57px;width:152px;height:26px;border-radius:13px;background:var(--white);font-size:10px;font-weight:700;color:#555;padding:7px 0 0 14px}
.search svg{position:absolute;right:10px;top:6px}
.main-nav{position:absolute;left:548px;top:136px;width:608px;display:flex;justify-content:space-between;font-size:10.5px;font-weight:700;color:var(--white);text-transform:uppercase}
.main-nav .active{border-bottom:2px solid var(--white);padding-bottom:3px}
.travel-form{position:absolute;left:681px;top:272px;width:438px;height:310px;background:rgba(45,45,50,.72);border:2px solid rgba(255,255,255,.7);border-radius:6px}
.ribbon{position:absolute;left:670px;top:300px;width:460px;height:52px}
.ribbon-title{position:absolute;left:670px;top:300px;width:460px;height:52px;text-align:center;font-family:"Merienda",cursive;font-weight:700;font-size:22px;color:var(--white);line-height:52px}
.field{position:absolute;height:30px;background:var(--field);color:var(--white);font-size:13px;padding:6px 12px}
.btn-tips{position:absolute;left:791px;top:519px;width:222px;height:32px;background:linear-gradient(180deg,#3eb6e6,#1f86b8);border-radius:3px;color:var(--white);font-weight:700;font-size:13px;text-align:center;line-height:32px}
.cat-nav{position:absolute;left:124px;top:654px;width:955px;display:flex;justify-content:space-between;font-family:"Fira Sans Condensed",sans-serif;font-weight:700;font-size:14px;color:var(--white);text-transform:uppercase}

/* Intro */
.intro{position:absolute;left:16px;top:697px;width:1168px;height:202px;background:var(--white)}
.intro p{position:absolute;left:0;top:78px;width:1168px;text-align:center;font-weight:700;font-size:28px;line-height:34px;color:var(--blue)}

/* Cards */
.card{position:absolute;left:56px;width:699px;height:475px;background:var(--white)}
.card h2{position:absolute;left:32px;top:30px;font-family:"Fira Sans Condensed",sans-serif;font-weight:600;font-size:25px;color:#555;text-transform:uppercase}
.card .media{position:absolute;left:29px;top:78px;width:641px;height:200px}
.card p{position:absolute;left:32px;top:294px;width:636px;font-size:13.5px;line-height:22px;color:var(--muted)}
.btn{position:absolute;background:var(--orange);color:var(--white);font-weight:700;font-size:13px;text-align:center;text-transform:uppercase}
.card .btn{left:510px;top:411px;width:160px;height:31px;line-height:31px}
.divider{position:absolute;left:56px;width:1086px;height:2px;border-top:2px dashed #9fd6ee}
.divider-mark{position:absolute;width:22px;height:22px;border-radius:50%;background:var(--blue-light);left:388px;top:-12px;box-shadow:0 0 0 10px var(--panel-bg)}

/* Sidebar */
.blog-box{position:absolute;left:804px;top:966px;width:333px;height:243px;background:var(--white)}
.blog-ribbon{position:absolute;left:775px;top:960px;width:390px;height:46px}
.blog-ribbon-title{position:absolute;left:775px;top:960px;width:390px;height:46px;line-height:46px;text-align:center;font-family:"Merienda",cursive;font-weight:700;font-size:17px;color:var(--white)}
.blog-list{position:absolute;left:822px;top:1033px;width:300px;list-style:none;font-size:14px;line-height:20px;color:#555}
.blog-list li{position:relative;padding-left:30px;margin-bottom:16px}
.blog-list svg{position:absolute;left:0;top:2px}
.ad{position:absolute;left:804px;width:333px}
.ad-title{position:absolute;left:0;width:333px;text-align:center;font-weight:700;color:var(--white);text-transform:uppercase;text-shadow:0 1px 3px rgba(0,0,0,.4)}

/* Feed */
.feed{position:absolute;left:61px;top:2600px;width:1078px;height:393px;display:grid;grid-template-columns:137px 135px 135px 270px 135px 135px 131px;grid-template-rows:132px 135px 126px;gap:0}

/* Footer */
.footer{position:absolute;left:16px;top:3011px;width:1168px;height:310px;background:linear-gradient(180deg,#e3f1f8 0%,#eef5f6 45%,#efe7da 100%)}
.footer-scene{position:absolute;left:0;top:0;width:1168px;height:310px}
.f-head{position:absolute;font-weight:700;font-size:13px;color:var(--blue);text-transform:uppercase}
.f-links{position:absolute;list-style:none;font-weight:700;font-size:11.5px;line-height:21px;color:#333;text-transform:uppercase}
.f-text{position:absolute;font-weight:600;font-size:11.5px;line-height:16px;color:#444}
.f-input{position:absolute;left:433px;top:155px;width:225px;height:34px;background:var(--white);font-size:12px;padding:10px 12px;color:#555}
.f-sub{position:absolute;left:433px;top:204px;width:102px;height:34px;background:var(--dark);color:var(--white);font-weight:700;font-size:11.5px;text-align:center;line-height:34px}
.social.foot{left:721px;top:200px;gap:10px}
.social.foot span{width:36px;height:36px;background:#555}
.f-brand{position:absolute;left:966px;top:120px;font-weight:700;font-size:50px;color:var(--orange);letter-spacing:-1px}
.copyright{position:absolute;left:16px;top:3321px;width:1168px;height:27px;background:var(--blue-light);color:var(--white);font-size:10px;font-weight:700;text-align:center;line-height:27px;text-transform:uppercase}
</style>
</head>
<body>
<div class="page"></div>

<header class="hero">
  <div class="hero-photo" role="img" aria-label="Sunset view over a historic seaside fort with a stone sentry box, palm trees and the waterfront"></div>
  <div class="brand">KVTvibe</div>
  <div class="social top" aria-label="Social links"><span></span><span></span><span></span><span></span><span></span></div>
  <div class="search">SEARCH SITE
    <svg width="14" height="14" viewBox="0 0 14 14"><circle cx="6" cy="6" r="4.5" fill="none" stroke="#888" stroke-width="1.6"/><line x1="9.3" y1="9.3" x2="13" y2="13" stroke="#888" stroke-width="1.8"/></svg>
  </div>
  <nav class="main-nav">
    <span class="active">Home</span><span>Events</span><span>Community Blog/Reviews</span><span>Maps</span><span>Get Involved</span><span>Surf &amp; Wind Reports</span><span>Contact</span>
  </nav>
  <svg class="hero-wave" viewBox="0 0 1168 60" preserveAspectRatio="none"><path d="M0 40 Q300 10 584 30 T1168 18 V60 H0Z" fill="#ffffff"/></svg>
</header>

<section class="travel-form-wrap">
  <div class="travel-form"></div>
  <svg class="ribbon" viewBox="0 0 460 52"><polygon points="0,6 22,6 22,46 0,46 10,26" fill="#1f86b8"/><polygon points="460,6 438,6 438,46 460,46 450,26" fill="#1f86b8"/><rect x="14" y="0" width="432" height="46" fill="#33a6d7"/></svg>
  <div class="ribbon-title">Discover the Beauty of KVT</div>
  <div class="field" style="left:703px;top:377px;width:195px">First Name</div>
  <div class="field" style="left:906px;top:377px;width:195px">Last Name</div>
  <div class="field" style="left:703px;top:422px;width:195px">Email Address</div>
  <div class="field" style="left:906px;top:422px;width:195px">Country</div>
  <div class="field" style="left:703px;top:465px;width:398px">When do you plan to visit KVT?</div>
  <div class="btn-tips">GET TRAVEL TIPS</div>
</section>

<nav class="cat-nav">
  <span>Historial Sites</span><span>Shopping</span><span>Getting Here &amp; Away</span><span>Restaurants</span><span>Live Entertainment</span><span>Places to Stay</span><span>Science</span><span>Real Estate</span>
</nav>

<section class="intro">
  <p>KVT area is a vibrant area in Northwest Puerto Rico with an airport,<br>many local restaurants, beautiful beaches, and many things to do.</p>
</section>

<main>
  <article class="card" style="top:953px">
    <h2>Historial Sites &amp; History of KVT</h2>
    <div class="media" role="img" aria-label="Modern arched convention building lit at dusk beside the water" style="background:linear-gradient(180deg,#7fa3c8 0%,#b9c6d3 40%,#4a5a6b 70%,#27323c 100%)"></div>
    <p>Lorem ipsum dolor sit amet, consectetuer adipiscing elit, sed diam nonummy nibh euismod tincidunt ut laoreet dolore magna aliquam erat volutpat. Ut wisi enim ad minim veniam, quis nostrud exerci tation ullamcorper suscipit lobortis nisl ut aliquip ex ea commodo consequat. Duis autem vel eum iriure dolor in hendrerit in vulputate velit esse molestie consequat, vel illum dolore eu feugiat nulla.</p>
    <div class="btn">Learn More</div>
  </article>
  <div class="divider" style="top:1465px"><span class="divider-mark"></span></div>

  <article class="card" style="top:1503px">
    <h2>Shopping Destinations in KVT</h2>
    <div class="media" role="img" aria-label="Friends walking along a shopping street carrying bags" style="background:linear-gradient(90deg,#d9d2c6 0%,#b59b84 35%,#efe9e2 55%,#8c7462 80%,#e8e4de 100%)"></div>
    <p>Lorem ipsum dolor sit amet, consectetuer adipiscing elit, sed diam nonummy nibh euismod tincidunt ut laoreet dolore magna aliquam erat volutpat. Ut wisi enim ad minim veniam, quis nostrud exerci tation ullamcorper suscipit lobortis nisl ut aliquip ex ea commodo consequat. Duis autem vel eum iriure dolor in hendrerit in vulputate velit esse molestie consequat, vel illum dolore eu feugiat nulla.</p>
    <div class="btn">Learn More</div>
  </article>
  <div class="divider" style="top:2013px"><span class="divider-mark"></span></div>

  <article class="card" style="top:2051px">
    <h2>Events</h2>
    <div class="media" role="img" aria-label="Historic coastal fortress on a green lawn above the sea" style="background:linear-gradient(180deg,#8fb3d6 0%,#c7d8e6 35%,#6f7a62 55%,#5f8c3a 80%,#4c7a2c 100%)"></div>
    <p>Lorem ipsum dolor sit amet, consectetuer adipiscing elit, sed diam nonummy nibh euismod tincidunt ut laoreet dolore magna aliquam erat volutpat. Ut wisi enim ad minim veniam, quis nostrud exerci tation ullamcorper suscipit lobortis nisl ut aliquip ex ea commodo consequat. Duis autem vel eum iriure dolor in hendrerit in vulputate velit esse molestie consequat, vel illum dolore eu feugiat nulla.</p>
    <div class="btn">Learn More</div>
  </article>
  <div class="divider" style="top:2566px"><span class="divider-mark" style="left:520px"></span></div>
</main>

<aside>
  <div class="blog-box"></div>
  <svg class="blog-ribbon" viewBox="0 0 390 46"><polygon points="0,6 22,6 22,42 0,42 10,24" fill="#1f86b8"/><polygon points="390,6 368,6 368,42 390,42 380,24" fill="#1f86b8"/><rect x="14" y="0" width="362" height="40" fill="#33a6d7"/></svg>
  <div class="blog-ribbon-title">Recent Blog Posts</div>
  <ul class="blog-list">
    <li><svg width="16" height="16" viewBox="0 0 16 16"><circle cx="6.5" cy="6.5" r="4.5" fill="none" stroke="#33a6d7" stroke-width="2"/><line x1="10" y1="10" x2="14" y2="14" stroke="#33a6d7" stroke-width="2"/></svg>How to Escape and Discover the KVT</li>
    <li><svg width="16" height="16" viewBox="0 0 16 16"><circle cx="6.5" cy="6.5" r="4.5" fill="none" stroke="#33a6d7" stroke-width="2"/><line x1="10" y1="10" x2="14" y2="14" stroke="#33a6d7" stroke-width="2"/></svg>Discover the Untold Stories of KVT area</li>
    <li><svg width="16" height="16" viewBox="0 0 16 16"><circle cx="6.5" cy="6.5" r="4.5" fill="none" stroke="#33a6d7" stroke-width="2"/><line x1="10" y1="10" x2="14" y2="14" stroke="#33a6d7" stroke-width="2"/></svg>My 10 Favorite Things to do in KVT</li>
  </ul>

  <div class="ad" style="top:1247px;height:321px">
    <div class="abs" role="img" aria-label="Colourful fishing boats pulled up on a sandy beach under a blue sky" style="inset:0;background:linear-gradient(180deg,#4fb2e3 0%,#8fd0ee 45%,#e8d9b8 62%,#b84a3a 78%,#e4d3b2 100%)"></div>
    <div class="ad-title" style="top:38px;font-size:17px;line-height:22px">Surf<br>&amp; Wind<br>Reports</div>
    <div class="btn" style="left:25px;top:118px;width:100px;height:28px;line-height:28px;font-size:11px">Learn More</div>
  </div>

  <div class="ad" style="top:1611px;height:245px">
    <div class="abs" role="img" aria-label="Group of friends enjoying drinks together outdoors" style="inset:0;background:linear-gradient(135deg,#3f8fb8 0%,#6fb3cf 40%,#c9b08a 75%,#8a6a4c 100%)"></div>
    <div class="ad-title" style="top:30px;font-size:17px;line-height:22px;width:220px">Find the Best Accomodation in the KVT</div>
    <div class="btn" style="left:25px;top:118px;width:100px;height:28px;line-height:28px;font-size:11px">Learn More</div>
  </div>

  <div class="ad" style="top:1899px;height:281px">
    <div class="abs" role="img" aria-label="Plates of local food and drinks on a wooden table" style="inset:0;background:linear-gradient(160deg,#5a3a24 0%,#7a5134 45%,#b78a4a 70%,#4a2e1c 100%)"></div>
    <div class="ad-title" style="top:78px;font-size:22px;line-height:26px">Restaurant<br>Ads</div>
    <div class="btn" style="left:66px;top:163px;width:200px;height:33px;line-height:33px">Learn More</div>
  </div>

  <div class="ad" style="top:2224px;height:304px">
    <div class="abs" role="img" aria-label="Live band performing on a dim stage" style="inset:0;background:linear-gradient(180deg,#1f1f24 0%,#3a3a44 50%,#1a1a1e 100%)"></div>
    <div class="ad-title" style="top:78px;font-size:21px;line-height:26px">Live Entertainment<br>Ads</div>
    <div class="btn" style="left:66px;top:168px;width:200px;height:33px;line-height:33px">Learn More</div>
  </div>
</aside>

<section class="feed" aria-label="Live hashtag feed">
  <div role="img" aria-label="Green field under a cloudy sky" style="grid-column:1/3;grid-row:1/3;background:linear-gradient(180deg,#6e8fae,#b9c5c7 45%,#5c7f3a 70%,#3f5f2a)"></div>
  <div role="img" aria-label="Evening street scene" style="background:linear-gradient(#2a2118,#5a4430)"></div>
  <div role="img" aria-label="Happiness is a three-day weekend poster" style="grid-row:1/3;background:linear-gradient(#f6c41c,#f0b000)"></div>
  <div role="img" aria-label="Grilled food platter" style="grid-column:5/7;background:linear-gradient(#3b2416,#8a4a24)"></div>
  <div role="img" aria-label="Old stone tower" style="background:linear-gradient(#b8c6c8,#7a5a3a)"></div>
  <div role="img" aria-label="Sunset over the water" style="grid-column:3;grid-row:2;background:linear-gradient(#7a8aa8,#d9905a)"></div>
  <div role="img" aria-label="People at an evening gathering" style="grid-column:5/8;grid-row:2/4;background:linear-gradient(#3a2818,#a86a3a 60%,#4a2e1a)"></div>
  <div role="img" aria-label="Yellow archway" style="grid-column:1;grid-row:3;background:linear-gradient(#e0a81a,#2a3a68)"></div>
  <div role="img" aria-label="Hacienda building" style="grid-column:2;grid-row:3;background:linear-gradient(#2a3a58,#c48a4a)"></div>
  <div role="img" aria-label="Dusk sky over trees" style="grid-column:3;grid-row:3;background:linear-gradient(#5a6a7a,#2a2a2a)"></div>
  <div role="img" aria-label="Crowd at an outdoor event" style="grid-column:4;grid-row:3;background:linear-gradient(90deg,#8a9aa8,#b8b0a0 50%,#c84a3a)"></div>
</section>

<footer class="footer">
  <div class="footer-scene" role="img" aria-label="Faded beach scene with lounge chairs on the sand"></div>
  <div class="f-head" style="left:40px;top:68px">Quick Links</div>
  <ul class="f-links" style="left:40px;top:92px"><li>Events</li><li>Community Blog</li><li>Maps</li><li>Get Involved</li><li>Surf &amp; Wind Reports</li><li>Historial Sites</li><li>Shopping</li></ul>
  <ul class="f-links" style="left:227px;top:92px"><li>Getting Here &amp; Away</li><li>Restaurants</li><li>Live Entertainment</li><li>Places to Stay</li><li>Science</li><li>Realestate</li><li>Contact</li></ul>
  <div class="f-head" style="left:433px;top:68px">Newsletter Sign Up</div>
  <div class="f-text" style="left:433px;top:96px;width:230px">Stay informed about our news by signing up for our Newsletters.</div>
  <div class="f-input">Email</div>
  <div class="f-sub">SUBSCRIBE</div>
  <div class="f-head" style="left:703px;top:68px">Contact</div>
  <div class="f-text" style="left:703px;top:96px">info@kvtvibe-demo.com</div>
  <div class="f-head" style="left:703px;top:162px">Be Social With Us</div>
  <div class="social foot" aria-label="Social links"><span></span><span></span><span></span><span></span><span></span></div>
  <div class="f-brand">KVTvibe</div>
</footer>
<div class="copyright">Copyright © 2016 KVT Vibe. All rights reserved.</div>
</body>
</html>
```